I need the following on my business card:
- Name: Dana Whitcomb
- License # 0M93216
- Title: Producer
- Phone: (555) 017-3904
- Email: Dana@CorbelInsuranceServices.com

- Company: Corbel Insurance Services
- Address: 27408 Larkmoor Ave Suite 610, Fairhollow, CA 90217
- Website: www.CorbelInsuranceServices.com

Also add our slogan on the card: "Steady Cover, Honest Advice"

```html
<!DOCTYPE html>
<html lang="en">
<head>
<meta charset="utf-8">
<title>Corbel Insurance Services – Business Card</title>
<link rel="stylesheet" href="https://fonts.googleapis.com/css2?family=Outfit:wght@400;500;600&family=Montserrat:ital,wght@1,400&display=swap">
<style>
  :root {
    --backdrop: #d4d5d5;
    --brand-green: #2eaa3e;
    --brand-navy: #232f7e;
    --card-white: #f4f4f2;
    --ink: #1f1f24;
    --on-green: #ffffff;
  }
  * { box-sizing: border-box; margin: 0; padding: 0; }
  html, body {
    width: 1200px; height: 1200px; overflow: hidden;
    background: var(--backdrop);
    font-family: "Outfit", sans-serif;
  }
  .card {
    position: absolute; top: 466px;
    width: 488px; height: 278px;
    border-radius: 28px; overflow: hidden;
  }
  .card-front { left: 80px; background: var(--brand-green); }
  .card-back { left: 635px; background: var(--card-white); }

  .wordmark {
    position: absolute; left: 0; right: 0; text-align: center;
    font-family: "Outfit", sans-serif;
  }
  .wordmark-name { display: block; font-size: 36px; font-weight: 600; letter-spacing: 1px; line-height: 1; color: var(--brand-navy); }
  .wordmark-sub { display: block; font-size: 13px; font-weight: 400; letter-spacing: 5px; margin-top: 8px; padding-left: 5px; }
  .card-front .wordmark { top: 110px; }
  .card-front .wordmark-sub { color: var(--on-green); }
  .card-back .wordmark { top: 55px; }
  .card-back .wordmark-sub { color: var(--brand-green); }

  .slogan {
    position: absolute; left: 0; right: 0; text-align: center;
    font-family: "Montserrat", sans-serif; font-style: italic; font-weight: 400;
  }
  .card-front .slogan { top: 207px; font-size: 12px; color: var(--on-green); }
  .card-back .slogan { top: 120px; font-size: 11px; color: var(--ink); }

  .holder { position: absolute; left: 41px; top: 158px; }
  .holder-name { font-size: 24px; font-weight: 500; color: var(--brand-navy); line-height: 1; }
  .holder-title { font-size: 22px; font-weight: 500; color: var(--brand-green); line-height: 1; margin-top: 4px; }

  .license-band {
    position: absolute; left: 0; top: 215px; width: 146px; height: 17px;
    background: var(--brand-green);
    clip-path: polygon(0 0, 140px 0, 146px 100%, 0 100%);
    color: var(--on-green); font-size: 10.5px; font-weight: 500;
    line-height: 17px; padding-left: 39px;
  }

  .contact-list { position: absolute; left: 240px; top: 162px; list-style: none; }
  .contact-item {
    display: flex; align-items: flex-start; gap: 8px;
    font-size: 11.5px; color: var(--ink); line-height: 14px; margin-bottom: 6px;
  }
  .contact-item svg { flex: none; width: 12px; height: 12px; margin-top: 1px; fill: var(--brand-green); }
</style>
</head>
<body>

<section class="card card-front" aria-label="Card front">
  <div class="wordmark">
    <span class="wordmark-name">CORBEL</span>
    <span class="wordmark-sub">INSURANCE SERVICES</span>
  </div>
  <p class="slogan">"Steady Cover, Honest Advice"</p>
</section>

<section class="card card-back" aria-label="Card back">
  <div class="wordmark">
    <span class="wordmark-name">CORBEL</span>
    <span class="wordmark-sub">INSURANCE SERVICES</span>
  </div>
  <p class="slogan">"Steady Cover, Honest Advice"</p>

  <div class="holder">
    <p class="holder-name">Dana Whitcomb</p>
    <p class="holder-title">Producer</p>
  </div>
  <div class="license-band">License # 0M93216</div>

  <ul class="contact-list">
    <li class="contact-item">
      <svg viewBox="0 0 24 24" aria-hidden="true"><path d="M6.6 10.8a15.1 15.1 0 0 0 6.6 6.6l2.2-2.2c.3-.3.7-.4 1-.2 1.1.4 2.3.6 3.6.6.6 0 1 .4 1 1V20c0 .6-.4 1-1 1A17 17 0 0 1 3 4c0-.6.4-1 1-1h3.5c.6 0 1 .4 1 1 0 1.3.2 2.5.6 3.6.1.3 0 .7-.2 1z"/></svg>
      <span>(555) 017-3904</span>
    </li>
    <li class="contact-item">
      <svg viewBox="0 0 24 24" aria-hidden="true"><path d="M2 5h20v14H2z M4 7v.4l8 5.3 8-5.3V7z" fill-rule="evenodd"/></svg>
      <span>Dana@CorbelInsuranceServices.com</span>
    </li>
    <li class="contact-item">
      <svg viewBox="0 0 24 24" aria-hidden="true"><path d="M12 2a7 7 0 0 0-7 7c0 5.3 7 13 7 13s7-7.7 7-13a7 7 0 0 0-7-7zm0 9.5A2.5 2.5 0 1 1 12 6.5a2.5 2.5 0 0 1 0 5z"/></svg>
      <span>27408 Larkmoor Ave Suite 610,<br>Fairhollow, CA 90217</span>
    </li>
    <li class="contact-item">
      <svg viewBox="0 0 24 24" aria-hidden="true"><path d="M12 2a10 10 0 1 0 0 20 10 10 0 0 0 0-20zm0 2c.9 1.2 1.6 2.6 2 4h-4c.4-1.4 1.1-2.8 2-4zM4.3 14a8 8 0 0 1 0-4h3.4a16 16 0 0 0 0 4zm.8 2h3c.3 1.3.8 2.5 1.4 3.6A8 8 0 0 1 5.1 16zm3-8h-3a8 8 0 0 1 4.4-3.6C8.9 5.5 8.4 6.7 8.1 8zM12 20c-.9-1.2-1.6-2.6-2-4h4c-.4 1.4-1.1 2.8-2 4zm2.3-6H9.7a14 14 0 0 1 0-4h4.6a14 14 0 0 1 0 4zm.2 5.6c.6-1.1 1.1-2.3 1.4-3.6h3a8 8 0 0 1-4.4 3.6zM16.3 14a16 16 0 0 0 0-4h3.4a8 8 0 0 1 0 4zm-.4-6c-.3-1.3-.8-2.5-1.4-3.6A8 8 0 0 1 18.9 8z"/></svg>
      <span>www.CorbelInsuranceServices.com</span>
    </li>
  </ul>
</section>

</body>
</html>
```